Redesign of WordHarbor.com in Bootstrap 4

Current design of WordHarbor.com is not responsive. We need to change it to latest version of Bootstrap 4 keeping essential elements in place.

Apart from home page, we need designs for http://www.wordharbor.com/meaning/cat also.

Coding

Coded - Design and coding required

Number of Pages Required

2 page

Colors
34a7d8

Requirements
Must have
• Bootstrap 4

```html
<!DOCTYPE html>
<html lang="en">
<head>
<meta charset="utf-8">
<title>WordHarbor.com</title>
<link href="https://fonts.googleapis.com/css2?family=Raleway:wght@400;500;600;700;800&display=swap" rel="stylesheet">
<style>
:root{
  --orange:#f39a16;
  --blue:#5cb6df;
  --dark:#3c3c3c;
  --nav:#4a4a4a;
  --footer:#343434;
  --panel:#f3f3f3;
  --text:#444;
  --white:#fff;
}
*{box-sizing:border-box;margin:0;padding:0}
html,body{width:776px;height:1200px;overflow:hidden}
body{font-family:'Raleway',sans-serif;color:var(--text);background:var(--white);position:relative;font-size:9px}
.abs{position:absolute}
.topline{left:0;top:0;width:776px;height:3px;background:var(--orange)}
.brand{left:76px;top:22px;display:flex;align-items:center;gap:6px}
.brand-mark{width:14px;height:14px;border-radius:50%;background:var(--orange)}
.brand-name{font-size:20px;font-weight:800;color:#1f6fb2;letter-spacing:.5px}
.login input{position:absolute;height:18px;border:1px solid #bbb;font:400 8.5px 'Raleway',sans-serif;padding:0 5px;color:#555;background:#fff}
.login .forgot{left:503px;top:43px;font-size:8px;color:#555}
.login .join{left:591px;top:43px;font-size:8px;color:#2a8fd0;font-weight:600}
.login .btn{left:663px;top:38px;width:49px;height:18px;background:var(--orange);color:#fff;font-size:8px;font-weight:700;display:flex;align-items:center;justify-content:center}
.nav{left:0;top:76px;width:776px;height:32px;background:linear-gradient(#555,#3f3f3f)}
.nav ul{list-style:none;position:absolute;left:64px;top:0;display:flex;height:32px}
.nav li{color:#fff;font-size:10.5px;display:flex;align-items:center;justify-content:center;border-right:1px solid #333;height:32px}
.nav li.active{background:var(--orange)}
.hero{left:0;top:108px;width:776px;height:370px;background:radial-gradient(ellipse at 50% 40%,#9a958e 0%,#6b6660 55%,#3b3835 100%)}
.hero h1{position:absolute;left:0;width:776px;top:56px;text-align:center;font-size:24px;font-weight:800;color:var(--orange)}
.hero .sub{position:absolute;left:0;width:776px;top:91px;text-align:center;font-size:8.5px;color:#eee}
.search{position:absolute;left:198px;top:125px;width:380px;height:34px;background:#fff;border:2px solid #ddd;display:flex;align-items:center}
.search span{flex:1;padding-left:8px;font-size:10px;color:#888}
.search b{width:80px;height:28px;margin-right:2px;background:var(--orange);color:#fff;font-weight:500;font-size:10px;display:flex;align-items:center;justify-content:center}
.hero .book{position:absolute;left:308px;top:194px;width:158px;height:158px;border-radius:14px;background:linear-gradient(#c0505e,#8e2a36)}
.hero svg.arrow{position:absolute;top:256px}
.features{left:64px;top:498px;width:648px;height:132px;background:var(--dark);color:#fff}
.features h2{position:absolute;left:38px;top:20px;font-size:14.5px;font-weight:500;color:var(--orange);display:flex;align-items:center;gap:8px}
.features ul{position:absolute;list-style:none;font-size:8.5px;line-height:12px}
.features li{position:relative;padding-left:12px;margin-bottom:8px}
.features li:before{content:"";position:absolute;left:0;top:4px;width:3px;height:3px;border-radius:50%;background:#fff}
.features .mascot{position:absolute;left:564px;top:8px;width:68px;height:114px;border-radius:34px;background:linear-gradient(#f2c92b,#3a3a3a)}
.card{width:307px;height:123px;background:var(--panel)}
.card .thumb{position:absolute;left:10px;top:14px;width:108px;height:95px;border:1px solid #ccc}
.card h3{position:absolute;left:133px;top:14px;width:161px;height:25px;background:var(--blue);color:#fff;font-size:10px;font-weight:600;padding-left:9px;display:flex;align-items:center}
.card p{position:absolute;left:133px;top:48px;width:161px;font-size:7.6px;line-height:11.5px;text-align:justify;color:#555}
.card .more{position:absolute;left:133px;top:92px;padding:3px 5px;border:1px solid #666;border-radius:3px;font-size:8px;color:#333;background:#fff}
.browse{left:115px;top:948px;display:flex;align-items:center;font-size:10px;color:#333}
.browse .lbl{margin-right:8px}
.browse span.l{width:15px;height:14px;border:1px solid #999;margin-right:2.5px;font-size:8.5px;display:flex;align-items:center;justify-content:center;color:#444}
.footer{left:0;top:986px;width:776px;height:214px;background:var(--footer);color:#ddd}
.footer h4{position:absolute;top:27px;font-size:12px;font-weight:500;color:#fff}
.footer ul{position:absolute;list-style:none}
.links li{font-size:9.5px;height:18.5px;display:flex;align-items:center;gap:8px}
.news .name{font-size:10.5px;color:#eee}
.news .txt{font-size:7.6px;line-height:11px;color:#ddd}
.news .av{position:absolute;left:0;top:0;width:16px;height:16px;border-radius:50%;background:#b58a74}
.contact div{position:absolute;font-size:9px;line-height:16px;display:flex;gap:6px}
.others li{font-size:8px;height:16px}
.social{position:absolute;left:613px;top:127px;display:flex;gap:6px}
.social span{width:16px;height:16px;border-radius:50%;background:#fff}
.footer .rule{position:absolute;left:64px;top:174px;width:648px;height:1px;background:#666}
.footer .copy{position:absolute;left:0;width:776px;top:188px;text-align:center;font-size:8px;color:#ddd}
</style>
</head>
<body>
<div class="abs topline"></div>

<header>
  <div class="abs brand"><span class="brand-mark"></span><span class="brand-name">WORD HARBOR</span></div>
  <div class="login">
    <input class="abs" style="left:503px;top:15px;width:100px" value="User Name" aria-label="User Name">
    <input class="abs" style="left:611px;top:15px;width:101px" value="Password" aria-label="Password">
    <span class="abs forgot">Forgot password?</span>
    <span class="abs join">Join for FREE!</span>
    <span class="abs btn">LOGIN</span>
  </div>
</header>

<nav class="abs nav">
  <ul>
    <li class="active" style="width:94px">Home</li>
    <li style="width:103px">Idioms</li>
    <li style="width:140px">Common Errors</li>
    <li style="width:120px">Crossword</li>
    <li style="width:89px">Blog</li>
    <li style="width:102px">Contact</li>
  </ul>
</nav>

<section class="abs hero" role="img" aria-label="Worn concrete wall and wooden floor backdrop">
  <h1>WORD HARBOR</h1>
  <div class="sub">Nemo enim ipsam voluptatem quia voluptas</div>
  <div class="search"><span>Enter a word or phrase...</span><b>Search</b></div>
  <svg class="arrow" style="left:236px" width="20" height="36" viewBox="0 0 20 36"><polyline points="18,2 2,18 18,34" fill="none" stroke="#fff" stroke-width="2"/></svg>
  <div class="book" role="img" aria-label="Red dictionary and thesaurus book icon"></div>
  <svg class="arrow" style="left:512px" width="20" height="36" viewBox="0 0 20 36"><polyline points="2,2 18,18 2,34" fill="none" stroke="#fff" stroke-width="2"/></svg>
</section>

<section class="abs features">
  <h2><svg width="11" height="11" viewBox="0 0 11 11"><circle cx="4.5" cy="4.5" r="3.3" fill="none" stroke="var(--orange)" stroke-width="1.8"/><line x1="7" y1="7" x2="10" y2="10" stroke="var(--orange)" stroke-width="2"/></svg>Search, Save and Master Words</h2>
  <ul style="left:40px;top:54px">
    <li>Search from more than 300,000 words and phrases</li>
    <li>Multiple usages to clarify the context</li>
    <li>Audio, phonetics, meanings, synonyms and antonyms</li>
  </ul>
  <ul style="left:350px;top:54px;width:200px">
    <li>Save the words to your personal deck and access from anywhere</li>
    <li>It's FREE</li>
  </ul>
  <div class="mascot" role="img" aria-label="Cartoon bee mascot giving a thumbs up"></div>
</section>

<article class="abs card" style="left:64px;top:656px">
  <div class="thumb" role="img" aria-label="Printed magazine page with words" style="background:linear-gradient(135deg,#efece6,#d8d2c8)"></div>
  <h3>DIGITAL MAGAZINES</h3>
  <p>"Gaffe" is a social blunder and "gaff" is a large hook. Be warned not to make the gaffe of mixing it up with gaff.</p>
  <span class="more">Read More</span>
</article>
<article class="abs card" style="left:405px;top:656px">
  <div class="thumb" role="img" aria-label="Crossword grid with a pencil" style="background:linear-gradient(135deg,#f4f4f4,#9a9a9a)"></div>
  <h3>DAILY CROSSWORD</h3>
  <p>Crossword Lovers!<br>Take this daily crossword challenge from Word Harbor.</p>
  <span class="more">Read More</span>
</article>
<article class="abs card" style="left:64px;top:794px">
  <div class="thumb" role="img" aria-label="Browser addon manager screenshot" style="background:linear-gradient(#e9eef6,#cfd9e8)"></div>
  <h3>BROWSER ADDON</h3>
  <p>"Gaffe" is a social blunder and "gaff" is a large hook. Be warned not to make the gaffe of mixing it up with gaff.</p>
  <span class="more">Read More</span>
</article>
<article class="abs card" style="left:405px;top:794px">
  <div class="thumb" role="img" aria-label="Mobile app screens shown side by side" style="background:linear-gradient(90deg,#3a4654,#e0654a,#3a4654)"></div>
  <h3>DESIGNED FOR MOBILE</h3>
  <p>Crossword Lovers!<br>Take this daily crossword challenge from Word Harbor.</p>
  <span class="more">Read More</span>
</article>

<div class="abs browse">
  <span class="lbl">Browse Dictionary:</span>
  <span class="l">A</span><span class="l">B</span><span class="l">C</span><span class="l">D</span><span class="l">E</span><span class="l">F</span><span class="l">G</span><span class="l">H</span><span class="l">I</span><span class="l">J</span><span class="l">K</span><span class="l">L</span><span class="l">M</span><span class="l">N</span><span class="l">O</span><span class="l">P</span><span class="l">Q</span><span class="l">R</span><span class="l">S</span><span class="l">T</span><span class="l">U</span><span class="l">V</span><span class="l">W</span><span class="l">X</span><span class="l">Y</span><span class="l">Z</span>
</div>

<footer class="abs footer">
  <h4 style="left:64px">WordHarbor.com</h4>
  <ul class="links" style="left:64px;top:55px">
    <li>&#8594; FAQ</li><li>&#8594; Contact</li><li>&#8594; Blog</li><li>&#8594; Privacy Policy</li><li>&#8594; Terms of Use</li>
  </ul>

  <h4 style="left:230px">Latest News</h4>
  <div class="news abs" style="left:230px;top:58px;width:140px">
    <span class="av" role="img" aria-label="Author avatar"></span>
    <div style="padding-left:24px"><div class="name">Mara Ellison</div><div class="txt">perspiciatis unde omnis iste error sit voluptatem</div></div>
  </div>
  <div class="news abs" style="left:230px;top:110px;width:140px">
    <span class="av" role="img" aria-label="Author avatar"></span>
    <div style="padding-left:24px"><div class="name">Toby Renner</div><div class="txt">perspiciatis unde omnis iste error sit voluptatem</div></div>
  </div>

  <h4 style="left:424px">Contact</h4>
  <div class="contact">
    <div style="left:424px;top:57px"><svg width="8" height="10" viewBox="0 0 8 10"><path d="M4 0a3.5 3.5 0 0 0-3.5 3.5C.5 6 4 10 4 10s3.5-4 3.5-6.5A3.5 3.5 0 0 0 4 0z" fill="#fff"/><circle cx="4" cy="3.5" r="1.2" fill="var(--footer)"/></svg><span>Design Headquarters<br>118 Harbor Lane<br>Leeds 0412</span></div>
    <div style="left:424px;top:108px"><svg width="8" height="10" viewBox="0 0 8 8"><path d="M1 0l2 2-1 1.5c.7 1.2 1.3 1.8 2.5 2.5L6 5l2 2-1.2 1C3.5 7.5.5 4.5 0 1.2z" fill="#fff"/></svg><span>+ 1800 4471 2093</span></div>
    <div style="left:424px;top:130px"><svg width="8" height="10" viewBox="0 0 8 8"><path d="M1 0l2 2-1 1.5c.7 1.2 1.3 1.8 2.5 2.5L6 5l2 2-1.2 1C3.5 7.5.5 4.5 0 1.2z" fill="#fff"/></svg><span>info@wordharbor.com</span></div>
  </div>

  <h4 style="left:611px">Others</h4>
  <ul class="others" style="left:612px;top:58px">
    <li>Popular Words</li><li>Common Errors in English</li><li>Test Prep Online</li>
  </ul>
  <div class="social"><span></span><span></span><span></span><span></span></div>

  <div class="rule"></div>
  <div class="copy">© 2015 Just WordHarbor. All Rights Reserved</div>
</footer>
</body>
</html>
```